PROPERTY MANAGEMENT AND REAL ESTATE

Target Market(s)

real estate owners and investors

Industry/Entity Type

Real Estate

Contact Information for Business Card

BRIGHT LANTERN PROPERTY MANAGEMENT GROUP, LLC
487 North Corwin Parkway
Suite 260
Marlow Cove, OR 97127

```html
<!DOCTYPE html>
<html lang="en">
<head>
<meta charset="utf-8">
<title>Bright Lantern Property Management Group – Business Card</title>
<link rel="stylesheet" href="https://fonts.googleapis.com/css2?family=Lato:wght@400;700&family=Carlito:wght@400;700&display=swap">
<style>
  :root {
    --brand-red: #8c1a1f;
    --brand-red-light: #a3383a;
    --card-white: #ebebeb;
    --ink: #1f1f1f;
    --backdrop: #d9d6d2;
    --heading-font: "Lato", sans-serif;
    --body-font: "Carlito", "Lato", sans-serif;
  }
  * { margin: 0; padding: 0; box-sizing: border-box; }
  html, body { width: 1200px; height: 900px; overflow: hidden; }
  body {
    background: var(--backdrop);
    position: relative;
    font-family: var(--body-font);
    color: var(--ink);
  }
  .card {
    position: absolute;
    top: 296px;
    width: 540px;
    height: 309px;
    overflow: hidden;
    box-shadow: 0 6px 18px rgba(0,0,0,0.18);
  }

  /* Front */
  .card-front { left: 40px; background: var(--card-white); }
  .front-edge {
    position: absolute; left: 0; top: 0; bottom: 0; width: 22px;
    background: var(--brand-red);
  }
  .brand-mark {
    position: absolute; left: 52px; top: 28px;
    width: 62px; height: 62px; border-radius: 50%;
    background: var(--brand-red);
  }
  .brand-name {
    position: absolute; left: 126px; top: 66px;
    font-family: var(--heading-font);
    font-weight: 400;
    font-size: 19px;
    line-height: 1.12;
    letter-spacing: 0.3px;
    color: var(--ink);
    text-transform: uppercase;
  }
  .employee {
    position: absolute; left: 52px; top: 118px;
  }
  .employee-name { color: var(--brand-red); font-size: 16px; line-height: 1.2; }
  .employee-title { font-size: 11px; letter-spacing: 0.5px; margin-top: 2px; }
  .website {
    position: absolute; left: 52px; top: 180px; font-size: 14px;
  }
  .website .domain { color: var(--brand-red); }
  .contact {
    position: absolute; left: 280px; top: 176px;
    font-size: 14.5px; line-height: 1.3;
  }
  .contact .label { color: var(--brand-red); margin-right: 3px; }

  /* Back */
  .card-back { left: 620px; background: var(--brand-red); }
  .back-disc {
    position: absolute; left: -70px; top: -150px;
    width: 330px; height: 330px; border-radius: 50%;
    background: var(--brand-red-light);
    opacity: 0.55;
  }
  .back-name {
    position: absolute; left: 210px; top: 196px;
    font-family: var(--heading-font);
    font-size: 20px; line-height: 1.15;
    letter-spacing: 0.4px;
    color: #f3eded;
    text-transform: uppercase;
  }
</style>
</head>
<body>
  <section class="card card-front" aria-label="Business card front">
    <div class="front-edge"></div>
    <span class="brand-mark"></span>
    <p class="brand-name">Bright Lantern Property<br>Management Group</p>
    <div class="employee">
      <p class="employee-name">Employee Name</p>
      <p class="employee-title">TITLE</p>
    </div>
    <p class="website">www.<span class="domain">brightlanternpm</span>.com</p>
    <div class="contact">
      <p><span class="label">T</span>555.204.7316</p>
      <p><span class="label">E</span>info@brightlanternpm.com</p>
      <p>487 North Corwin Parkway Suite 260</p>
      <p>Marlow Cove, OR 97127</p>
    </div>
  </section>

  <section class="card card-back" aria-label="Business card back">
    <div class="back-disc"></div>
    <p class="back-name">Bright Lantern Property<br>Management Group</p>
  </section>
</body>
</html>
```